Redesign of Smart Watch Gift Voucher-SEE ATTACHED CURRENT DESIGN

I need to redesign my existing design using all same content and elements.

MY ENVISION: I invision more of a professional advertisement type of flyer/voucher. Imagine how Corvel.com would create a professionally looking flyer promoting the lumo or veno.

you can get many ideas about professional design by looking at some of corvels flyer designs :
https://www.findora-example.net/search?q=lumo+advertisment&mode=img&ref=a83kd02mzq7

stock photos are attached, you do not have to use them all, you can use some or none i am open to your designs using your own images if you want...just make sure the smartwatch looks black

DO NOT LEAVE ANY CONTENT OR ELEMENTS OUT ON MOCK UP PLEASE

SEE ATTACHED CURRENT DESIGN

I need to redesign my existing design using all same content and elements. DO NOT LEAVE ANY CONTENT OR ELEMENTS OUT ON MOCK UP PLEASE

Target Market(s)

B2B-you can get many ideas about professional design by looking at some of corvels flyer designs :

Industry/Entity Type

Marketing

Requirements
Must have
• I need to redesign my existing design using all same content and elements. DO NOT LEAVE ANY CONTENT OR ELEMENTS OUT ON MOCK UP PLEASE

Nice to have

Should not have

```html
<!DOCTYPE html>
<html lang="en">
<head>
<meta charset="utf-8">
<title>Smartwatch Reward Voucher</title>
<link rel="stylesheet" href="https://fonts.googleapis.com/css2?family=Montserrat:ital,wght@0,300;0,400;0,500;0,600;0,700;1,700;1,900&family=Playfair+Display:ital,wght@1,700&display=swap">
<style>
:root{
  --stage:#182b5c;
  --indigo:#2e3192;
  --banner:#3c3fa3;
  --ink:#111111;
  --navy:#141a3a;
  --rim:#3434b4;
  --muted:#aeb3cf;
  --paper:#ffffff;
  --feature-ink:#1b1f3b;
}
*{margin:0;padding:0;box-sizing:border-box}
html,body{width:1200px;height:1044px;overflow:hidden;background:var(--stage)}
body{position:relative;font-family:"Montserrat",sans-serif}
.flyer{position:absolute;left:196.6px;top:0;width:1163px;height:1505px;background:var(--paper);overflow:hidden;transform:scale(0.69369);transform-origin:0 0}
.flyer > *{position:absolute}
.dots{top:65px;height:138px;width:258px}
.dots-left{left:0;background:linear-gradient(90deg,var(--indigo) 0%,rgba(46,49,146,.5) 45%,rgba(46,49,146,0) 100%);opacity:.55}
.dots-right{right:0;background:linear-gradient(270deg,var(--indigo) 0%,rgba(46,49,146,.5) 45%,rgba(46,49,146,0) 100%);opacity:.55}
.kicker{left:0;right:0;top:62px;text-align:center;font-family:"Playfair Display",serif;font-style:italic;font-weight:700;font-size:54px;color:var(--indigo);letter-spacing:.5px}
.headline{left:0;right:0;top:120px;text-align:center;font-family:"Montserrat",sans-serif;font-style:italic;font-weight:900;font-size:86px;color:var(--ink);letter-spacing:-1px;line-height:1}
.intro{left:115px;right:90px;top:225px;text-align:center;font-size:15px;font-weight:500;line-height:18.5px;color:var(--ink)}
.banner{left:74px;top:297px;width:1023px;height:66px}
.banner svg{position:absolute;inset:0}
.banner p{position:relative;text-align:center;line-height:66px;color:#fff;font-style:italic;font-weight:700;font-size:30px;letter-spacing:.8px;word-spacing:6px}
.hero{left:310px;top:330px;width:853px;height:700px;border-radius:0 0 0 60px;background:
  radial-gradient(ellipse 180px 230px at 290px 470px,#1c1c1f 0%,#2b2b30 60%,rgba(43,43,48,0) 100%),
  radial-gradient(ellipse 210px 270px at 600px 470px,rgba(92,160,220,.55) 0%,rgba(150,200,240,.25) 60%,rgba(255,255,255,0) 100%),
  radial-gradient(ellipse 320px 300px at 560px 230px,#c9ccd4 0%,#e7e8ec 55%,rgba(255,255,255,0) 100%)}
.icons{left:225px;top:380px;display:flex;gap:55px}
.icons svg{width:44px;height:52px;fill:none;stroke:var(--banner);stroke-width:3.4;stroke-linecap:round;stroke-linejoin:round}
.rule{left:175px;top:448px;width:815px;border-top:2px dashed #8c8fa8}
.features{left:68px;top:478px}
.features h2{font-size:31px;font-weight:700;color:var(--feature-ink);letter-spacing:.5px;margin-bottom:16px}
.features ul{list-style:none}
.features li{display:flex;align-items:center;gap:10px;height:34.3px;font-size:19.5px;font-weight:500;color:var(--feature-ink);letter-spacing:.3px}
.features li svg{width:22px;height:22px;fill:none;stroke:var(--feature-ink);stroke-width:2}
.base{left:0;top:0;width:1163px;height:1505px}
.how{left:75px;top:1100px;width:532px;color:#fff}
.how h3,.quotes h3{font-size:31px;font-weight:600;letter-spacing:1.2px;margin-bottom:10px}
.how p{font-size:15.5px;font-weight:300;line-height:18.5px;text-align:justify;color:var(--muted)}
.quotes{left:645px;top:1100px;width:450px;color:#fff}
.quotes p{font-size:15.5px;font-weight:300;line-height:18.5px;color:var(--muted)}
.quotes cite{display:block;font-style:normal;font-weight:700;font-size:15.5px;color:var(--muted)}
.voucher{left:80px;top:1285px;width:985px;height:173px}
.voucher svg{position:absolute;inset:0}
.cert{position:absolute;left:160px;top:40px;color:var(--navy)}
.cert .label{font-size:15px;font-weight:400;color:#4a4f6a}
.cert .value{font-size:20px;font-weight:500;letter-spacing:.5px;margin-bottom:14px}
.redeem{position:absolute;left:295px;right:40px;top:42px;text-align:center;color:var(--navy)}
.redeem .lead{font-size:17px;font-weight:500;letter-spacing:.3px}
.redeem .url{font-size:24.5px;font-weight:500;letter-spacing:1px;margin:10px 0 6px}
.redeem .terms{font-size:14.5px;color:#6a6f88;letter-spacing:.4px}
</style>
</head>
<body>
<main class="flyer">
  <div class="dots dots-left" role="img" aria-label="Halftone dot pattern fading to the right"></div>
  <div class="dots dots-right" role="img" aria-label="Halftone dot pattern fading to the left"></div>

  <p class="kicker">ENJOY YOUR BRAND NEW</p>
  <h1 class="headline">SMARTWATCH</h1>
  <p class="intro">Congratulations, you have been rewarded with a Brand New Smart Fitness Watch shipped right to your door. Just payship-ping and handling. Your new Smart Fitness Watch has these features: sport mode, pedometer, distance, calorie, heartrate, blood pressure, stopwatch, sleep monitoring, phone locator, reminders, remote camera, an alarm clock and muchmore!</p>

  <div class="hero" role="img" aria-label="Black smartwatch showing a running icon beside a woman sprinting through blue light streaks, with a faded large watch face in the background"></div>

  <div class="banner">
    <svg viewBox="0 0 1023 66" preserveAspectRatio="none"><polygon points="0,0 1023,0 1000,33 1023,66 0,66 23,33" fill="var(--banner)"/></svg>
    <p>Take Control of Your Life with Your New Smart Watch</p>
  </div>

  <div class="icons">
    <svg viewBox="0 0 44 52"><circle cx="22" cy="28" r="14"/><path d="M22 20v8l6 4M8 14l6-5M36 14l-6-5M13 42l-3 5M31 42l3 5"/></svg>
    <svg viewBox="0 0 44 52"><circle cx="30" cy="10" r="4"/><path d="M26 17l-6 12 8 5-3 12M20 29l-8 8M22 19l-9 3-3 6M26 20l5 7 7-2M2 24h8M4 30h8M6 36h6"/></svg>
    <svg viewBox="0 0 44 52"><path d="M12 6c2 10 0 16 2 22s-4 14-2 20M32 6c-2 10 0 16-2 22s4 14 2 20M14 28c4-4 12-4 16 0M16 40h12"/></svg>
    <svg viewBox="0 0 44 52"><circle cx="22" cy="6" r="4"/><path d="M22 12v16l6 12M22 20l-6 6M22 20l6 4M22 28l-6 14M10 48h22M30 40v8"/></svg>
    <svg viewBox="0 0 44 52"><path d="M18 4h10M18 10h10M23 10v30M14 34h18M18 40h10M12 46h8"/></svg>
    <svg viewBox="0 0 44 52"><circle cx="30" cy="20" r="4"/><path d="M8 30l12-8 10 6M4 38c5-4 9 4 14 0s9 4 14 0 9 4 10 2M4 45c5-4 9 4 14 0s9 4 14 0 9 4 10 2"/></svg>
    <svg viewBox="0 0 52 52"><path d="M4 12v30M4 34h44v8M4 26h44v8M12 26v-6h14v6"/></svg>
    <svg viewBox="0 0 48 52"><circle cx="11" cy="36" r="8"/><circle cx="37" cy="36" r="8"/><circle cx="30" cy="12" r="3.5"/><path d="M11 36l9-12 8 6 9 6M20 24l8-4"/></svg>
  </div>
  <div class="rule"></div>

  <section class="features">
    <h2>FEATURES</h2>
    <ul>
      <li><svg viewBox="0 0 22 22"><circle cx="11" cy="11" r="9.5"/><path d="M6.5 11.5l3 3 6-6.5"/></svg>Pedometer</li>
      <li><svg viewBox="0 0 22 22"><circle cx="11" cy="11" r="9.5"/><path d="M6.5 11.5l3 3 6-6.5"/></svg>Calorie Counter</li>
      <li><svg viewBox="0 0 22 22"><circle cx="11" cy="11" r="9.5"/><path d="M6.5 11.5l3 3 6-6.5"/></svg>Blood Pressure Monitor</li>
      <li><svg viewBox="0 0 22 22"><circle cx="11" cy="11" r="9.5"/><path d="M6.5 11.5l3 3 6-6.5"/></svg>Sleep Monitoring</li>
      <li><svg viewBox="0 0 22 22"><circle cx="11" cy="11" r="9.5"/><path d="M6.5 11.5l3 3 6-6.5"/></svg>Reminders Feature</li>
      <li><svg viewBox="0 0 22 22"><circle cx="11" cy="11" r="9.5"/><path d="M6.5 11.5l3 3 6-6.5"/></svg>Alarm Clock</li>
      <li><svg viewBox="0 0 22 22"><circle cx="11" cy="11" r="9.5"/><path d="M6.5 11.5l3 3 6-6.5"/></svg>Distance Tracker</li>
      <li><svg viewBox="0 0 22 22"><circle cx="11" cy="11" r="9.5"/><path d="M6.5 11.5l3 3 6-6.5"/></svg>Heart Rate Monitor</li>
      <li><svg viewBox="0 0 22 22"><circle cx="11" cy="11" r="9.5"/><path d="M6.5 11.5l3 3 6-6.5"/></svg>Stopwatch</li>
      <li><svg viewBox="0 0 22 22"><circle cx="11" cy="11" r="9.5"/><path d="M6.5 11.5l3 3 6-6.5"/></svg>Phone Locator</li>
      <li><svg viewBox="0 0 22 22"><circle cx="11" cy="11" r="9.5"/><path d="M6.5 11.5l3 3 6-6.5"/></svg>Remote Camera</li>
      <li><svg viewBox="0 0 22 22"><circle cx="11" cy="11" r="9.5"/><path d="M6.5 11.5l3 3 6-6.5"/></svg>Waterproof</li>
    </ul>
  </section>

  <svg class="base" viewBox="0 0 1163 1505" aria-hidden="true">
    <defs>
      <linearGradient id="rimGlow" x1="0" x2="1">
        <stop offset="0" stop-color="var(--rim)"/>
        <stop offset=".5" stop-color="#2a2aa0"/>
        <stop offset="1" stop-color="var(--rim)"/>
      </linearGradient>
    </defs>
    <path d="M0 1050 Q581 870 1163 1085 L1163 1505 L0 1505Z" fill="url(#rimGlow)"/>
    <path d="M0 1100 Q581 880 1163 1100 L1163 1505 L0 1505Z" fill="var(--navy)"/>
  </svg>

  <section class="how">
    <h3>HOW CAN WE DO THIS?</h3>
    <p>We have a couple retail partners that we team up with to "crowd purchase" huge shipping containers that hold 10's of thousands of electronicproducts at 80-90% off retail. We simply pass our savings on to you as we do not profit from our electronic products. You are basically able to"piggy back" on our partnerships and buying power to get an attractive electronic premium for a fraction of the retail cost.</p>
  </section>

  <section class="quotes">
    <h3>WHAT OTHERS SAY</h3>
    <p>"Are you sure this is not a Norvik Orbit Smartwatch in DISGUISE???? I love mine."</p>
    <cite>Dale M. Seabrook Bay, NJ</cite>
  </section>

  <div class="voucher">
    <svg viewBox="0 0 985 173">
      <polygon points="2,2 983,2 962,86 983,171 2,171 23,86" fill="none" stroke="#fff" stroke-width="2" stroke-dasharray="4 4"/>
      <polygon points="10,9 975,9 954,86 975,164 10,164 31,86" fill="var(--paper)"/>
      <line x1="295" y1="12" x2="295" y2="162" stroke="var(--navy)" stroke-width="2" stroke-dasharray="4 4"/>
    </svg>
    <div class="cert">
      <p class="label">Certificate ID</p>
      <p class="value">91772-89218</p>
      <p class="label">Expires</p>
      <p class="value">10/03/2020</p>
    </div>
    <div class="redeem">
      <p class="lead">view all the details of this special offer and redeem online at</p>
      <p class="url">WWW.PERKVAULTREWARDS.COM</p>
      <p class="terms">*Terms and Conditions apply see website for details</p>
    </div>
  </div>
</main>
</body>
</html>
```